QuillBackDesk Website Redesign

I'm looking to redesign our website QuillBackDesk.com. The main goal is to give it a fresh design that is easy on the eyes and pushes the users to creating an account.

Our platform is very simple and we only do one thing, we use ai to generate response to customer and product reviews.

See attached file to see the pricing section style.

On the homepage just under the hero section, I would like to include the wording:
"Write replies to the reviews you get on sites like:" then show the logos like we have on our register page: https://app.quillbackdesk.com/public/index.php

Target Market(s)

Business owners with brick and morter business or any business or product that gets online reviews

Industry/Entity Type

reputation management

Number of Pages Required

2 page

Requirements
Must have
• Home page and pricing page

```html
<!DOCTYPE html>
<html lang="en">
<head>
<meta charset="utf-8">
<title>QuillBackDesk — AI Replies To Your Reviews</title>
<link href="https://fonts.googleapis.com/css2?family=Poppins:wght@400;500;600;700&family=Inter:wght@400;500;600;700;800&display=swap" rel="stylesheet">
<style>
:root{
  --navy:#1f3a93;
  --navy-deep:#1b2f7a;
  --royal:#2447b0;
  --orange:#f5a623;
  --ink:#1d1d1d;
  --muted:#444a5a;
  --pale:#eef2fc;
  --white:#ffffff;
}
*{box-sizing:border-box;margin:0;padding:0}
html,body{width:1200px;height:4252px;overflow:hidden}
body{font-family:"Inter",Arial,sans-serif;color:var(--ink);background:var(--white);position:relative}
.abs{position:absolute}
section,header,footer{position:absolute;left:0;width:1200px}

/* header */
.site-header{top:0;height:110px}
.brand{left:110px;top:24px;display:flex;align-items:center;gap:10px}
.brand-mark{width:62px;height:54px;border:5px solid var(--navy);border-radius:8px;background:var(--white)}
.brand-name{font-family:"Poppins",sans-serif;font-weight:700;color:var(--navy);font-size:26px;line-height:1}
.brand-name small{display:block;font-size:13px;font-weight:500;color:var(--orange);margin-bottom:2px}
.nav{left:540px;top:44px;display:flex;font-size:12px;color:#222}
.nav a{color:#222;text-decoration:none;margin-right:40px}
.btn{display:inline-flex;align-items:center;justify-content:center;font-weight:700;text-decoration:none;font-size:12px;color:var(--white)}
.btn-navy{background:var(--navy)}
.btn-orange{background:var(--orange)}
.nav-cta{left:975px;top:33px;width:116px;height:39px}

/* hero */
.hero-band{top:395px;height:272px;background:var(--navy-deep)}
.hero-card{left:66px;top:117px;width:1067px;height:390px;background:var(--pale);border-radius:34px}
.hero-title{left:44px;top:76px;font-size:44px;line-height:47px;font-weight:700;color:var(--navy)}
.hero-title .lead{color:var(--orange);font-weight:400}
.hero-btns{left:44px;top:237px;display:flex;gap:12px}
.hero-btns .btn{height:40px;font-size:11px}
.hero-tag{left:40px;top:330px;font-size:15px;color:var(--navy);letter-spacing:.2px;display:flex;align-items:center;gap:10px}
.star{color:var(--orange);font-size:14px}
.hero-art{left:680px;top:40px;width:320px;height:270px;border-radius:20px;background:linear-gradient(135deg,#dfe6fb,#f7c35a 75%,#2a4bb6)}
.platforms{top:507px;height:160px;display:flex}
.platform{flex:1;display:flex;align-items:center;justify-content:center;color:var(--white);font-family:"Poppins",sans-serif;font-weight:600;font-size:28px;background:var(--navy-deep)}
.platform + .platform{border-left:3px solid #e8ecf8}

/* benefits */
.benefits{top:667px;height:610px}
.sec-title{text-align:center;font-size:36px;line-height:40px;font-weight:600;color:var(--navy)}
.sec-title .lead{color:var(--orange);font-weight:400;display:block}
.underline{width:54px;height:5px;background:var(--orange);margin:8px auto 0;border-radius:3px}
.benefits .sec-title{position:absolute;left:0;width:1200px;top:60px}
.card{position:absolute;top:226px;width:227px;height:317px;background:var(--white);border-radius:12px;box-shadow:0 4px 14px rgba(31,58,147,.16);text-align:center;padding:0 14px}
.card-art{width:140px;height:120px;margin:34px auto 0;border-radius:12px;background:linear-gradient(135deg,#dbe3fb,#f6c04e)}
.card h3{font-size:15px;font-weight:700;margin-top:24px}
.card p{font-size:10.5px;line-height:16px;color:var(--muted);margin-top:34px}

/* how it works */
.how{top:1277px;height:880px;background:var(--pale)}
.how .sec-title{position:absolute;top:60px;width:1200px}
.how .sec-title .lead{display:inline}
.timeline{left:599px;top:135px;width:2px;height:745px;background:#5a6b9c}
.timeline-dot{left:594px;top:132px;width:12px;height:12px;background:var(--orange);border-radius:50%}
.step-num{width:42px;height:42px;border-radius:50%;background:var(--navy);color:var(--white);font-size:12px;font-weight:700;display:flex;align-items:center;justify-content:center;box-shadow:0 0 0 7px #c9d2ee;left:579px}
.step{width:320px}
.step h4{color:var(--orange);font-size:14px;font-weight:600}
.step .bar{width:36px;height:4px;background:var(--navy);margin:16px 0 18px}
.step h5{color:var(--navy);font-size:13px;font-weight:700;margin-bottom:6px}
.step p{font-size:11px;line-height:18px;color:#333}
.step-art{border-radius:16px;background:linear-gradient(135deg,#2a4bb6,#f6c04e)}

/* pricing */
.pricing{top:2157px;height:926px;background:linear-gradient(180deg,#2343a7 0%,#15266a 45%,#0b1020 100%)}
.pricing-title{top:60px;width:1200px;text-align:center;color:var(--white);font-size:36px;line-height:42px;font-weight:400}
.pricing-title b{font-weight:700}
.pricing-sub{top:155px;width:1200px;text-align:center;color:#e4e9ff;font-size:12px}
.pricing .underline{position:absolute;left:573px;top:180px;margin:0}
.plan{top:218px;width:446px;height:635px;background:var(--white);border-radius:10px;overflow:hidden}
.plan-head{height:112px;background:var(--pale);text-align:center;padding-top:34px}
.plan-head h3{color:var(--navy);font-size:22px;font-weight:600}
.plan-head p{font-size:11px;color:#333;margin-top:24px}
.plan-price{text-align:center;font-size:19px;font-weight:700;margin-top:26px}
.slider-labels{display:flex;justify-content:space-between;padding:0 56px;font-weight:700;font-size:15px;margin-top:22px}
.slider{position:relative;margin:24px 56px 0;height:8px;background:#dde4f6;border-radius:4px}
.slider i{position:absolute;left:0;top:0;width:82px;height:8px;background:var(--navy);border-radius:4px}
.slider b{position:absolute;left:70px;top:-8px;width:24px;height:24px;border-radius:50%;background:var(--white);border:2px solid var(--navy)}
.credits{text-align:center;font-size:15px;margin-top:30px}
.plan-btn{display:flex;margin:22px 56px 0;height:46px;font-size:16px;font-weight:600}
.plan-btn.orange{background:linear-gradient(90deg,#f8b930,#fccd53);color:var(--white)}
.plan-btn.navy{background:var(--royal);color:var(--white)}
.features{list-style:none;margin:24px 0 0 56px}
.features li{display:flex;align-items:center;gap:14px;font-size:15px;color:#222;height:44px}

/* faq */
.faq{top:3083px;height:507px}
.faq .sec-title{position:absolute;left:560px;width:80px;top:60px}
.faq .sec-title .lead{display:inline}
.faq-art{left:0;top:167px;width:508px;height:270px;border-radius:18px;background:linear-gradient(135deg,#dfe6fb,#7c93dc 55%,#f6c04e)}
.faq-list{left:578px;top:150px;width:510px}
.faq-item{display:flex;align-items:center;justify-content:space-between;background:var(--white);box-shadow:0 3px 10px rgba(0,0,0,.1);border-radius:6px;padding:0 44px;font-size:12px;color:#222;margin-bottom:30px;min-height:52px}
.faq-item span{max-width:390px;line-height:16px}

/* cta */
.cta{top:3590px;height:378px;background:#111b40}
.cta h2{top:105px;width:1200px;text-align:center;color:var(--white);font-size:42px;line-height:48px;font-weight:700}
.cta p{top:213px;width:1200px;text-align:center;color:#dde3ff;font-size:13px}
.cta .bar{left:572px;top:240px;width:56px;height:5px;background:var(--white);border-radius:3px}
.cta .btn{left:529px;top:270px;width:141px;height:38px;font-size:11px}

/* footer */
.site-footer{top:3968px;height:284px}
.site-footer .brand{left:110px;top:68px}
.site-footer .brand-mark{width:74px;height:60px}
.site-footer .brand-name{font-size:24px}
.site-footer .brand-name small{font-size:14px}
.foot-links{left:440px;top:72px;font-size:13px;font-weight:600;color:var(--navy);line-height:22px}
.foot-contact{left:605px;top:72px;font-size:13px;font-weight:600;color:var(--navy);line-height:18px}
.foot-contact .row{display:flex;gap:12px;margin-bottom:28px}
.follow{left:920px;top:72px;font-size:13px;font-weight:600;color:var(--navy)}
.socials{display:flex;gap:16px;margin-top:12px}
.socials i{width:40px;height:40px;border-radius:50%;background:var(--navy)}
.socials i.alt{background:var(--orange)}
.foot-rule{left:110px;top:210px;width:980px;height:2px;background:#b8c3e6}
.copy{top:240px;width:1200px;text-align:center;font-size:13px;font-weight:600;color:var(--navy)}
</style>
</head>
<body>

<header class="site-header">
  <div class="brand abs"><div class="brand-mark"></div><div class="brand-name"><small>★★★★★</small>QuillBackDesk</div></div>
  <nav class="nav abs"><a href="#">Why Reply?</a><a href="#">How It Works</a><a href="#">Pricing</a><a href="#">Blog</a><a href="#">Login</a></nav>
  <a class="btn btn-navy nav-cta abs" href="#">TRY FREE</a>
</header>

<section class="hero-band"></section>
<div class="hero-card abs">
  <h1 class="hero-title abs"><span class="lead">Write Personalized</span><br>Responses To Reviews<br>In 10 Seconds! (NO JOKE)</h1>
  <div class="hero-btns abs"><a class="btn btn-navy" href="#" style="width:160px">START FOR FREE</a><a class="btn btn-orange" href="#" style="width:130px">LEARN MORE</a></div>
  <div class="hero-tag abs"><span class="star">★ ★</span>WRITE REPLIES TO THE REVIEWS YOU GET ON SITES LIKE<span class="star">★ ★</span></div>
  <div class="hero-art abs" role="img" aria-label="Illustration of a person on a beanbag with a laptop surrounded by review and chat bubbles"></div>
</div>
<section class="platforms">
  <div class="platform">Searchly</div><div class="platform">Yapper</div><div class="platform">Craftly</div><div class="platform">TrustPost</div><div class="platform">Amzora</div><div class="platform">Stayhaus</div><div class="platform">Tripnotes</div>
</section>

<section class="benefits">
  <h2 class="sec-title"><span class="lead">It's Simple. Our Tool Writes Replies</span>And Responses To The Reviews Your Customers<br>Leave. Doesn't Matter If It's 1 Or 5 Stars.<div class="underline"></div></h2>
  <div class="card" style="left:110px"><div class="card-art" role="img" aria-label="Illustration of people working on SEO"></div><h3>Improved SEO</h3><p>Search Engines Love Seeing You Leave A Reply To Your Reviews And Will Give You A Boost In Their Search Results And Local SEO.</p></div>
  <div class="card" style="left:360px"><div class="card-art" role="img" aria-label="Illustration of people with a star rating"></div><h3>Build Customer Trust</h3><p>Customers want to know there are humans behind your companies product or service. Show them you value their time.</p></div>
  <div class="card" style="left:612px"><div class="card-art" role="img" aria-label="Illustration of a happy customer on a stage"></div><h3>Increase Customer Loyalty</h3><p>Search Engines Love Seeing You Leave A Reply To Your Reviews And Will Give You A Boost In Their Search Results And Local SEO.</p></div>
  <div class="card" style="left:863px"><div class="card-art" role="img" aria-label="Illustration of a support agent at a computer"></div><h3>Convert New Customers</h3><p>Search Engines Love Seeing You Leave A Reply To Your Reviews And Will Give You A Boost In Their Search Results And Local SEO.</p></div>
</section>

<section class="how">
  <h2 class="sec-title"><span class="lead">How</span> It Works<div class="underline"></div></h2>
  <div class="timeline abs"></div><div class="timeline-dot abs"></div>
  <div class="step-art abs" style="left:280px;top:150px;width:215px;height:190px" role="img" aria-label="Illustration of people signing up on a large phone"></div>
  <div class="step-num abs" style="top:225px">01</div>
  <div class="step abs" style="left:691px;top:180px"><h4>Step #1 Create An Account</h4><div class="bar"></div><h5>1 Minute Account Creation</h5><p>Gain Access To The Most Powerful Tool For Writing Unique And Personal Responses To The Reviews Your Customers Leave Your Business.</p></div>
  <div class="step abs" style="left:258px;top:420px"><h4>STEP #2 Copy And Paste The Review</h4><div class="bar"></div><h5>We make it way too simple!</h5><p>Just Copy The Customer Review And Paste<br>It Into Your Account Dashboard</p></div>
  <div class="step-num abs" style="top:455px">02</div>
  <div class="step-art abs" style="left:705px;top:375px;width:215px;height:200px" role="img" aria-label="Illustration of a person pasting a review into a dashboard"></div>
  <div class="step-art abs" style="left:262px;top:613px;width:245px;height:200px" role="img" aria-label="Illustration of people around a screen of generated responses"></div>
  <div class="step-num abs" style="top:692px">03</div>
  <div class="step abs" style="left:691px;top:648px"><h4>STEP #3 Personalized Response In Seconds</h4><div class="bar"></div><h5>Only a 10 second wait</h5><p>In Just Seconds You'll Receive 3 Unique And Personal Responses. Choose The Reply You Like Best Or Tell Our System To Generate 3 More.</p></div>
</section>

<section class="pricing">
  <h2 class="pricing-title abs">Never Worry About Having To Come Up With<br><b>A Unique Response To Each Review Ever Again!</b></h2>
  <p class="pricing-sub abs">If Your Business, Product Or Service Receives Reviews, This Tool Will Save You Hundreds Of Hours.</p>
  <div class="underline"></div>
  <div class="plan abs" style="left:110px">
    <div class="plan-head"><h3>Monthly Subscriptions</h3><p>Perfect For Getting Started For One Business/product</p></div>
    <div class="plan-price">Starts At $9.99 / Month</div>
    <div class="slider-labels"><span>50K</span><span>700K+</span></div>
    <div class="slider"><i></i><b></b></div>
    <div class="credits"><b>5000</b> word credits</div>
    <a class="btn plan-btn orange" href="#">Start For Free</a>
    <ul class="features">
      <li><svg width="20" height="16" viewBox="0 0 20 16"><path d="M2 8l6 6L18 2" fill="none" stroke="#1f3a93" stroke-width="3"/></svg>Personalized responses</li>
      <li><svg width="20" height="16" viewBox="0 0 20 16"><path d="M2 8l6 6L18 2" fill="none" stroke="#1f3a93" stroke-width="3"/></svg>30+ Languages</li>
      <li><svg width="20" height="16" viewBox="0 0 20 16"><path d="M2 8l6 6L18 2" fill="none" stroke="#1f3a93" stroke-width="3"/></svg>Auto-Save</li>
      <li><svg width="20" height="16" viewBox="0 0 20 16"><path d="M2 8l6 6L18 2" fill="none" stroke="#1f3a93" stroke-width="3"/></svg>Revision History</li>
      <li><svg width="20" height="16" viewBox="0 0 20 16"><path d="M2 8l6 6L18 2" fill="none" stroke="#1f3a93" stroke-width="3"/></svg>Assign members usage limits</li>
    </ul>
  </div>
  <div class="plan abs" style="left:644px">
    <div class="plan-head"><h3>Agency Subscriptions</h3><p>Perfect For Multiple Clients/products Per Month</p></div>
    <div class="plan-price">Starting at $75.00 / month</div>
    <a class="btn plan-btn navy" href="#" style="margin-top:56px">Start For Free</a>
    <ul class="features" style="margin-top:16px">
      <li><svg width="20" height="16" viewBox="0 0 20 16"><path d="M2 8l6 6L18 2" fill="none" stroke="#1f3a93" stroke-width="3"/></svg>Everything in the Startup plan</li>
      <li><svg width="20" height="16" viewBox="0 0 20 16"><path d="M2 8l6 6L18 2" fill="none" stroke="#1f3a93" stroke-width="3"/></svg>Dedicated Account Manager</li>
      <li><svg width="20" height="16" viewBox="0 0 20 16"><path d="M2 8l6 6L18 2" fill="none" stroke="#1f3a93" stroke-width="3"/></svg>Onboarding &amp; Training</li>
      <li><svg width="20" height="16" viewBox="0 0 20 16"><path d="M2 8l6 6L18 2" fill="none" stroke="#1f3a93" stroke-width="3"/></svg>Unlimited Integrations</li>
    </ul>
  </div>
</section>

<section class="faq">
  <h2 class="sec-title"><span class="lead">F</span>AQ<div class="underline"></div></h2>
  <div class="faq-art abs" role="img" aria-label="Illustration of a support agent at a desk with a large FAQ magnifier"></div>
  <div class="faq-list abs">
    <div class="faq-item"><span>Why Is It Important To Respond To Searchly Reviews?</span><svg width="14" height="9" viewBox="0 0 14 9"><path d="M1 1l6 6 6-6" fill="none" stroke="#1f3a93" stroke-width="2"/></svg></div>
    <div class="faq-item"><span>Why is it important to respond to negative reviews?</span><svg width="14" height="9" viewBox="0 0 14 9"><path d="M1 1l6 6 6-6" fill="none" stroke="#1f3a93" stroke-width="2"/></svg></div>
    <div class="faq-item"><span>How Can I Trust Someone Who Doesn't Work At My Business To Reply To Reviews On My Behalf?</span><svg width="14" height="9" viewBox="0 0 14 9"><path d="M1 1l6 6 6-6" fill="none" stroke="#1f3a93" stroke-width="2"/></svg></div>
    <div class="faq-item"><span>Which Online Review Sites Does QuillBackDesk.com Support?</span><svg width="14" height="9" viewBox="0 0 14 9"><path d="M1 1l6 6 6-6" fill="none" stroke="#1f3a93" stroke-width="2"/></svg></div>
  </div>
</section>

<section class="cta">
  <svg class="abs" style="left:278px;top:38px" width="644" height="240" viewBox="0 0 644 240"><path d="M440 200 H622 Q634 200 634 188 V22 Q634 10 622 10 H22 Q10 10 10 22 V188 Q10 200 22 200 H100 M540 200 L578 226 L600 200" fill="none" stroke="#2b4fc0" stroke-width="10" stroke-linejoin="round"/></svg>
  <h2 class="abs">Ready to give<br>QuillBackDesk a try?</h2>
  <p class="abs">Get started today with one FREE Reply to your Review. No credit card required.</p>
  <div class="bar abs"></div>
  <a class="btn btn-orange abs" href="#">TRY FOR FREE</a>
</section>

<footer class="site-footer">
  <div class="brand abs"><div class="brand-mark"></div><div class="brand-name"><small>★★★★★</small>QuillBackDesk</div></div>
  <div class="foot-links abs">Blog<br>Privacy Policy<br>Contact<br>Sitemap</div>
  <div class="foot-contact abs">
    <div class="row"><svg width="16" height="20" viewBox="0 0 16 20"><path d="M8 19s7-7 7-11A7 7 0 0 0 1 8c0 4 7 11 7 11z" fill="none" stroke="#f5a623" stroke-width="2"/><circle cx="8" cy="8" r="2.5" fill="#f5a623"/></svg><span>Location Name Will Be Here<br>Near This Building 12345</span></div>
    <div class="row"><svg width="18" height="18" viewBox="0 0 18 18"><path d="M4 1l3 4-2 2c1 3 3 5 6 6l2-2 4 3-2 3C8 17 1 10 1 3z" fill="none" stroke="#f5a623" stroke-width="1.8"/></svg><span>Phone:- 000-555-0147</span></div>
  </div>
  <div class="follow abs">Follow Us<div class="socials"><i aria-label="Social link A"></i><i class="alt" aria-label="Social link B"></i><i aria-label="Social link C"></i></div></div>
  <div class="foot-rule abs"></div>
  <p class="copy abs">©2023 QuillBackDesk.com All Rights Reserved</p>
</footer>

</body>
</html>
```